文章は添付のテキストのコピペで構いません。
見本の挨拶状はモノクロで、またテキストのみの、
硬い、暗い印象ですので、こちらを女性らしく、
可愛らしく、読みやすくしてください。

お手紙風(便箋風)など良いかもしれません。

初めて商品を手にした方に、買ってよかったと思われる、
ご挨拶状にしたいと思います。
縦書、横書き指定ございません。
記載項目
商品写真、ロゴ、電話番号、営業時間など

```html
<!DOCTYPE html>
<html lang="ja">
<head>
<meta charset="utf-8">
<title>ごあいさつ</title>
<link rel="stylesheet" href="https://fonts.googleapis.com/css2?family=Shippori+Mincho:wght@500&family=Zen+Maru+Gothic:wght@400;500&display=swap">
<style>
  :root {
    --paper: #fbf0f1;
    --paper-deep: #f6e2e5;
    --ink: #5a4446;
    --ink-soft: #7a6466;
    --title: #6a4b4e;
    --rose: #e58d9c;
    --pink: #f2b3bd;
    --peach: #f4b98f;
    --coral: #ee9a86;
    --lilac: #c9a9d6;
    --leaf: #b9c99a;
    --bottle: #5a2a22;
  }
  * { margin: 0; padding: 0; box-sizing: border-box; }
  html, body { width: 846px; height: 1200px; overflow: hidden; }
  body {
    background: var(--paper);
    font-family: "Zen Maru Gothic", sans-serif;
    color: var(--ink);
  }
  .letter {
    position: relative;
    width: 846px;
    height: 1200px;
    background: linear-gradient(180deg, var(--paper) 0%, #fcf3f4 60%, var(--paper-deep) 100%);
  }
  .floral-border {
    position: absolute;
    left: 0; top: 0;
    width: 846px; height: 330px;
    background: linear-gradient(100deg,
      var(--pink) 0%, var(--peach) 12%, var(--rose) 22%, var(--lilac) 32%,
      var(--coral) 42%, var(--pink) 52%, var(--leaf) 60%, var(--peach) 70%,
      var(--rose) 80%, var(--lilac) 90%, var(--coral) 100%);
    -webkit-mask-image: radial-gradient(ellipse 440px 250px at 50% 330px, transparent 78%, #000 100%);
            mask-image: radial-gradient(ellipse 440px 250px at 50% 330px, transparent 78%, #000 100%);
  }
  .title {
    position: absolute;
    top: 124px; left: 0; width: 100%;
    text-align: center;
    font-family: "Shippori Mincho", serif;
    font-weight: 500;
    font-size: 24px;
    letter-spacing: 0.3em;
    color: var(--title);
  }
  .message {
    position: absolute;
    top: 186px; left: 90px; width: 666px;
    text-align: center;
    font-size: 11px;
    line-height: 21px;
    color: var(--ink);
  }
  .message p { margin-bottom: 25px; }
  .message .lead { font-size: 12px; color: var(--title); }
  .closing {
    position: absolute;
    top: 950px; left: 110px; width: 450px;
    text-align: center;
    font-size: 11px;
    line-height: 20px;
  }
  .closing p { margin-bottom: 12px; }
  .product-photo {
    position: absolute;
    left: 700px; top: 905px;
    width: 100px; height: 270px;
    border-radius: 22px 22px 10px 10px;
    background: linear-gradient(90deg, #3e1a15, var(--bottle) 40%, #7a4034 60%, #3e1a15);
  }
  .footer {
    position: absolute;
    left: 40px; top: 1122px; width: 650px;
    display: flex; align-items: flex-start; gap: 22px;
  }
  .brands { display: flex; align-items: center; gap: 18px; padding-top: 8px; }
  .brand {
    display: flex; align-items: center; gap: 6px;
    font-size: 20px; font-weight: 500; color: var(--title);
  }
  .brand .dot { width: 10px; height: 10px; border-radius: 50%; background: var(--rose); }
  .contact { font-size: 9.5px; line-height: 17px; color: var(--ink-soft); white-space: nowrap; }
  .contact strong { color: var(--ink); font-weight: 500; }
</style>
</head>
<body>
<main class="letter">
  <div class="floral-border" role="img" aria-label="上部と左右を縁取る水彩のピンク・ピーチ・ラベンダー色の花々"></div>

  <h1 class="title">ごあいさつ</h1>

  <section class="message">
    <p>この度は、数多くのシャンプーの中より、<br>フルーレ「リュミエール ヘアシャンプーN」をお選びくださいまして誠にありがとうございます。</p>
    <p class="lead">「髪は女の命」。</p>
    <p>艶のある豊かな髪は、それだけで女性を美しく、若々しく見せてくれます。</p>
    <p>細かい毛穴や頭皮の汚れを丁寧に落とすことで、髪本来のハリとコシを取り戻し、<br>ボリュームのある美しい髪へと導きます。日々の洗髪こそが、<br>健やかな髪を育てるいちばんの近道だと私たちは考えております。</p>
    <p>髪のことは、年齢とともに気になってくるものです。だからこそ毎日のケアに、<br>やさしく確かなものを選んでいただきたい。そんな想いを込めました。</p>
    <p>本品には髪と頭皮に嬉しい天然由来の成分を贅沢に配合しております。<br>洗うたびに頭皮をすこやかに整え、指通りのなめらかな髪へ。<br>「髪のためのスキンケア」として、エイジングケアにお役立てください。</p>
    <p>美しい髪を手に入れるには、「頭皮の環境」と「髪の芯」を整えることが何よりも大切です。<br>洗髪だけではなく、乾かし方やブラッシングなど、毎日の習慣もぜひ見直してみてください。<br>ひとつひとつの積み重ねが、見違えるような髪へとつながっていきます。<br>私たちはこれからも、皆さまの髪の悩みに寄り添う商品づくりを続けてまいります。</p>
    <p>そこで皆さまのために、天然の植物エキスをたっぷりと配合した、頭皮とエイジングケアをここにご用意しました。</p>
    <p>また、スカルプケアや日々のお手入れについてのご相談も承っております。<br>お気軽にお問い合わせいただき、ご自身の髪にあったケアを見つけてください。<br>皆さまのお悩みにひとつでもお応えできれば幸いです。</p>
    <p>ご使用の際に気になる点がございましたら、下記のお客様窓口までご連絡ください。<br>スタッフ一同、心よりお待ちしております。</p>
  </section>

  <section class="closing">
    <p>頭皮のケアは、美しい髪を育てる。</p>
    <p>お客様にいつまでも輝いていただけるよう、<br>私たちも心を込めてサポートしてまいります。<br>今後ともどうぞよろしくお願い申し上げます。</p>
  </section>

  <div class="product-photo" role="img" aria-label="リュミエール ヘアシャンプーN のポンプボトルの商品写真"></div>

  <footer class="footer">
    <div class="brands">
      <span class="brand"><span class="dot"></span>Fleuret</span>
      <span class="brand">LUMIE</span>
    </div>
    <div class="contact">
      <strong>フルーレ お客様サポート</strong><br>
      フリーダイヤル：0120-000-123（月〜金 10:00〜18:00 土日祝祭日除く）<br>
      メール：care@fleuret-hair.jp
    </div>
  </footer>
</main>
</body>
</html>
```